Corporate Business Card

Very professional, Modern, Not to busy, include phone address email, website
(253) 555-0174, 61807 19th Street N, Kent, WA 98517, marcus@kestrelbayholding.com, brelvanindustries.com

Target Market(s)

Manufacturing

Industry/Entity Type

Aero, machining, manufacturing, Off road racing

Contact Information for Business Card

Phone, address email, website

```html
<!DOCTYPE html>
<html lang="en">
<head>
<meta charset="utf-8">
<title>Brelvan Industries – Business Card</title>
<link href="https://fonts.googleapis.com/css2?family=Montserrat:wght@400;500;700;800&display=swap" rel="stylesheet">
<style>
  :root {
    --navy: #1a3670;
    --navy-deep: #14295a;
    --red: #d7222b;
    --white: #ffffff;
    --paper: #f7f7f7;
    --ink: #1d1d1f;
    --stage: #e6e7ea;
  }
  * { box-sizing: border-box; margin: 0; padding: 0; }
  html, body {
    width: 1200px; height: 900px; overflow: hidden;
    background: var(--stage);
    font-family: "Montserrat", sans-serif;
  }
  .canvas {
    width: 1200px; height: 900px;
    display: flex; flex-direction: column; align-items: center; justify-content: center;
    gap: 40px;
  }
  .card {
    width: 700px; height: 400px;
    border-radius: 22px;
    position: relative; overflow: hidden;
    box-shadow: 0 10px 28px rgba(0,0,0,.18);
  }

  /* Back side */
  .card--back {
    background: var(--navy);
    display: flex; align-items: center; justify-content: center;
  }
  .card--back .brand-name {
    color: var(--white);
    font-weight: 800;
    font-size: 54px;
    letter-spacing: 1px;
    display: flex; align-items: center; gap: 16px;
  }
  .brand-mark {
    width: 22px; height: 22px; background: var(--red); display: inline-block;
  }

  /* Front side */
  .card--front { background: var(--paper); }
  .front-logo {
    position: absolute; left: 48px; top: 150px; width: 270px;
  }
  .front-logo .brand-name {
    color: var(--navy);
    font-weight: 800;
    font-size: 30px;
    line-height: 1.15;
    display: flex; align-items: center; gap: 12px;
  }
  .front-logo .brand-mark { width: 16px; height: 16px; flex: none; }
  .divider {
    position: absolute; left: 345px; top: 95px;
    width: 2px; height: 190px; background: var(--navy);
  }
  .contact {
    position: absolute; left: 372px; top: 92px;
    color: var(--ink);
  }
  .person-name {
    font-weight: 800; font-size: 30px; letter-spacing: 1px; color: var(--navy);
    line-height: 1;
  }
  .person-name .surname { color: var(--red); }
  .person-role { font-size: 17px; font-weight: 500; margin: 6px 0 14px; }
  .address { font-size: 16px; font-weight: 500; line-height: 1.3; margin-bottom: 12px; }
  .contact-list { list-style: none; font-size: 16px; font-weight: 500; }
  .contact-list li { display: flex; align-items: center; gap: 10px; margin-bottom: 6px; }
  .contact-list svg { width: 16px; height: 16px; flex: none; }
  .web-domain { color: var(--navy); }
  .swoosh { position: absolute; left: 0; bottom: 0; width: 700px; height: 110px; }
</style>
</head>
<body>
<main class="canvas">

  <section class="card card--back" aria-label="Business card back">
    <div class="brand-name"><span class="brand-mark"></span>Brelvan Industries</div>
  </section>

  <section class="card card--front" aria-label="Business card front">
    <div class="front-logo">
      <div class="brand-name"><span class="brand-mark"></span>Brelvan Industries</div>
    </div>
    <div class="divider"></div>

    <div class="contact">
      <h1 class="person-name">MARCUS <span class="surname">HALE</span></h1>
      <p class="person-role">Owner</p>
      <p class="address">61807 19th Street N, Kent<br>WA 98517</p>
      <ul class="contact-list">
        <li>
          <svg viewBox="0 0 24 24" aria-hidden="true"><path fill="#d7222b" d="M6.6 10.8a15.1 15.1 0 0 0 6.6 6.6l2.2-2.2a1 1 0 0 1 1-.25 11.4 11.4 0 0 0 3.6.57 1 1 0 0 1 1 1V20a1 1 0 0 1-1 1A17 17 0 0 1 3 4a1 1 0 0 1 1-1h3.5a1 1 0 0 1 1 1c0 1.25.2 2.45.57 3.57a1 1 0 0 1-.25 1z"/></svg>
          (253) 555-0174
        </li>
        <li>
          <svg viewBox="0 0 24 24" aria-hidden="true"><path fill="#d7222b" d="M2 5h20v14H2z"/><path d="M2 5l10 8 10-8" fill="none" stroke="#fff" stroke-width="2"/></svg>
          marcus@kestrelbayholding.com
        </li>
        <li>
          <svg viewBox="0 0 24 24" aria-hidden="true"><g fill="none" stroke="#d7222b" stroke-width="2"><circle cx="12" cy="12" r="9"/><path d="M3 12h18M12 3c3 3.5 3 14.5 0 18M12 3c-3 3.5-3 14.5 0 18"/></g></svg>
          www.<span class="web-domain">brelvanindustries</span>.com
        </li>
      </ul>
    </div>

    <svg class="swoosh" viewBox="0 0 700 110" preserveAspectRatio="none" aria-hidden="true">
      <path d="M0 20 C 250 30, 480 60, 700 105 L700 110 L0 110 Z" fill="#d7222b"/>
      <path d="M0 32 C 250 40, 480 70, 700 110 L0 110 Z" fill="#ffffff"/>
      <path d="M0 40 C 260 46, 500 76, 700 60 L700 110 L0 110 Z" fill="#1a3670"/>
    </svg>
  </section>

</main>
</body>
</html>
```